Ridgeline Outfitters Business Cards

Recently had a logo done with Artfolio and now looking for a business card to go along with it.

Target Market(s)

Ridgeline Outfitters is a weapons dealer. My market will be primarily men, hunting, shooting type.

Industry/Entity Type

Business

Contact Information for Business Card

I selected double sided, but this is not required, single or double is going to be fine. I picture the logo on one side, or perhaps just the circle which contains "RO" with the remaining info on the other side.

Font styles to use
Sans Serif

Requirements
Must have
• My name: Milo Brandt
• Title: Owner
• tel: 612-555-0187
• web: www.ridgelineoutfittersmn.example
Nice to have
• I like the concept of a black business card. I would like to keep the colors monotone, black, grey, white or red. Red is acceptable because it is in the logo. I have also seen cards that are matte black with shiny black as well, perhaps for the logo (or circle RO) part of the logo.
• I will upload a couple of the logos for use, and also an example I just found of the black on black. and some others that have a nice contrast.
Should not have
• lots of colors are not wanted.

```html
<!DOCTYPE html>
<html lang="en">
<head>
<meta charset="utf-8">
<title>Ridgeline Outfitters Business Cards</title>
<link rel="stylesheet" href="https://fonts.googleapis.com/css2?family=Arimo:wght@400;700&display=swap">
<style>
  :root {
    --backdrop: #d3d4d6;
    --card-light: #ffffff;
    --card-dark: #343434;
    --brand-red: #ed1c24;
    --brand-grey: #6f6f71;
    --ink: #111111;
    --muted: #8a8a8c;
    --dark-ink: #0a0a0a;
    --dark-muted: #a9a9ab;
  }
  * { box-sizing: border-box; margin: 0; padding: 0; }
  html, body { width: 1200px; height: 902px; overflow: hidden; }
  body {
    position: relative;
    background: var(--backdrop);
    font-family: "Arimo", Arial, sans-serif;
  }
  .card {
    position: absolute;
    width: 466px;
    height: 251px;
    border-radius: 17px;
    overflow: hidden;
    box-shadow: 0 14px 18px -8px rgba(0,0,0,0.35);
  }
  .card--light { background: var(--card-light); }
  .card--dark { background: var(--card-dark); }
  .card--front-light { left: 105px; top: 93px; }
  .card--back-light { left: 611px; top: 194px; }
  .card--front-dark { left: 124px; top: 457px; }
  .card--back-dark { left: 630px; top: 558px; }

  .tab {
    position: absolute;
    top: 74px;
    width: 19px;
    height: 103px;
    background: var(--brand-red);
  }
  .tab--left { left: 0; border-radius: 0 12px 12px 0; }
  .tab--right { right: 0; border-radius: 12px 0 0 12px; }
  .card--dark .tab { background: var(--dark-ink); }

  .mark-ring { position: absolute; }
  .mark-ring--small { left: 53px; top: 82px; width: 88px; height: 88px; }
  .mark-ring--large { left: -10px; top: -6px; width: 206px; height: 206px; }

  .brand-name {
    position: absolute;
    left: 165px;
    top: 114px;
    font-weight: 700;
    font-size: 21px;
    letter-spacing: 0.5px;
    color: var(--brand-red);
    white-space: nowrap;
  }
  .card--dark .brand-name { color: var(--dark-ink); }

  .contact { position: absolute; left: 212px; top: 81px; }
  .contact__name {
    font-weight: 700;
    font-size: 19px;
    color: var(--ink);
    letter-spacing: 0.2px;
  }
  .contact__title { font-size: 14px; color: var(--muted); margin-top: 2px; }
  .contact__list { list-style: none; margin-top: 16px; }
  .contact__item {
    display: flex;
    align-items: center;
    gap: 7px;
    font-size: 12px;
    color: var(--muted);
    height: 21px;
    white-space: nowrap;
  }
  .contact__icon { width: 14px; height: 14px; flex: none; }
  .card--dark .contact__name { color: var(--dark-ink); }
  .card--dark .contact__title,
  .card--dark .contact__item { color: var(--dark-muted); }
</style>
</head>
<body>

  <section class="card card--light card--front-light">
    <div class="tab tab--left"></div>
    <svg class="mark-ring mark-ring--small" viewBox="0 0 88 88" aria-hidden="true">
      <circle cx="44" cy="44" r="40" fill="none" stroke="var(--brand-grey)" stroke-width="7"/>
    </svg>
    <p class="brand-name">RIDGELINE OUTFITTERS</p>
  </section>

  <section class="card card--light card--back-light">
    <svg class="mark-ring mark-ring--large" viewBox="0 0 214 214" aria-hidden="true">
      <circle cx="107" cy="107" r="95" fill="none" stroke="var(--brand-grey)" stroke-width="10"/>
    </svg>
    <div class="tab tab--right"></div>
    <div class="contact">
      <p class="contact__name">MILO BRANDT</p>
      <p class="contact__title">Owner</p>
      <ul class="contact__list">
        <li class="contact__item">
          <svg class="contact__icon" viewBox="0 0 14 14" aria-hidden="true">
            <rect width="14" height="14" rx="2" fill="var(--brand-red)"/>
            <path d="M4.2 3.2l1.6 0.1 0.7 2-1 0.8c0.5 1.1 1.3 1.9 2.4 2.4l0.8-1 2 0.7 0.1 1.6c-0.3 0.7-1 1-1.7 0.9C6.3 10.4 3.6 7.7 3.3 4.9c-0.1-0.7 0.2-1.4 0.9-1.7z" fill="#fff"/>
          </svg>
          612-555-0187
        </li>
        <li class="contact__item">
          <svg class="contact__icon" viewBox="0 0 14 14" aria-hidden="true">
            <rect width="14" height="14" rx="2" fill="var(--brand-red)"/>
            <circle cx="7" cy="7" r="3.8" fill="none" stroke="#fff" stroke-width="1.1"/>
            <path d="M3.2 7h7.6M7 3.2c-1.4 2.3-1.4 5.3 0 7.6M7 3.2c1.4 2.3 1.4 5.3 0 7.6" fill="none" stroke="#fff" stroke-width="0.9"/>
          </svg>
          www.ridgelineoutfittersmn.example
        </li>
      </ul>
    </div>
  </section>

  <section class="card card--dark card--front-dark">
    <div class="tab tab--left"></div>
    <svg class="mark-ring mark-ring--small" viewBox="0 0 88 88" aria-hidden="true">
      <circle cx="44" cy="44" r="40" fill="none" stroke="var(--dark-ink)" stroke-width="7"/>
    </svg>
    <p class="brand-name">RIDGELINE OUTFITTERS</p>
  </section>

  <section class="card card--dark card--back-dark">
    <svg class="mark-ring mark-ring--large" viewBox="0 0 214 214" aria-hidden="true">
      <circle cx="107" cy="107" r="95" fill="none" stroke="var(--dark-ink)" stroke-width="10"/>
    </svg>
    <div class="tab tab--right"></div>
    <div class="contact">
      <p class="contact__name">MILO BRANDT</p>
      <p class="contact__title">Owner</p>
      <ul class="contact__list">
        <li class="contact__item">
          <svg class="contact__icon" viewBox="0 0 14 14" aria-hidden="true">
            <rect x="0.6" y="0.6" width="12.8" height="12.8" rx="2" fill="none" stroke="var(--dark-ink)" stroke-width="1.2"/>
            <path d="M4.2 3.2l1.6 0.1 0.7 2-1 0.8c0.5 1.1 1.3 1.9 2.4 2.4l0.8-1 2 0.7 0.1 1.6c-0.3 0.7-1 1-1.7 0.9C6.3 10.4 3.6 7.7 3.3 4.9c-0.1-0.7 0.2-1.4 0.9-1.7z" fill="var(--dark-ink)"/>
          </svg>
          612-555-0187
        </li>
        <li class="contact__item">
          <svg class="contact__icon" viewBox="0 0 14 14" aria-hidden="true">
            <rect x="0.6" y="0.6" width="12.8" height="12.8" rx="2" fill="none" stroke="var(--dark-ink)" stroke-width="1.2"/>
            <circle cx="7" cy="7" r="3.6" fill="none" stroke="var(--dark-ink)" stroke-width="1.1"/>
            <path d="M3.4 7h7.2M7 3.4c-1.3 2.2-1.3 5 0 7.2M7 3.4c1.3 2.2 1.3 5 0 7.2" fill="none" stroke="var(--dark-ink)" stroke-width="0.9"/>
          </svg>
          www.ridgelineoutfittersmn.example
        </li>
      </ul>
    </div>
  </section>

</body>
</html>
```